Wexmoor Digest - our client magazine

A quality magazine consisting of a number of bespoke articles in the first half followed by an overview of each company that form part of the group as well as details of the services offered. Vast majority of the copy is attached to provide a good overview of the content required. The magazine will require printing so quality imagery is required.

Industry/Entity Type

Recruitment

Font styles to use
Serif

Colors
0355a3
6b449b
3276b5
876aae
a64599
00a990
5c5c5c
000000
474747

Requirements
Must have
• Bringing the copy to life through flow charts and/or diagrams where possible.

```html
<!DOCTYPE html>
<html lang="en">
<head>
<meta charset="utf-8">
<title>Wexmoor Digest – 10 Steps to Success</title>
<link rel="stylesheet" href="https://fonts.googleapis.com/css2?family=Montserrat:wght@600;700&family=Oswald:wght@500;600&family=Tinos:wght@400;700&display=swap">
<style>
  :root {
    --blue: #0355a3;
    --blue-mid: #3276b5;
    --ink: #000000;
    --ink-soft: #474747;
    --grey: #5c5c5c;
    --paper: #ffffff;
    --stage: #e6e6e6;
    --sky: #b9cad9;
  }
  * { box-sizing: border-box; margin: 0; padding: 0; }
  html, body { width: 1200px; height: 880px; overflow: hidden; background: var(--stage); }
  .spread {
    position: absolute; left: 60px; top: 40px; width: 1080px; height: 800px;
    display: flex; box-shadow: 0 6px 24px rgba(0,0,0,.15);
  }
  .page { position: relative; width: 540px; height: 800px; background: var(--paper); overflow: hidden; }
  .page--left { box-shadow: inset -18px 0 22px -18px rgba(0,0,0,.18); }
  .page--right { box-shadow: inset 18px 0 22px -18px rgba(0,0,0,.18); }

  .hero-photo {
    position: absolute; left: 0; top: 0; width: 300px; height: 800px;
    background: linear-gradient(180deg, #f3f1ee 0%, #e7e2dc 22%, #c9b89f 38%, #8fa3b7 60%, #6f88a0 80%, #a9bccd 100%);
    -webkit-mask-image: linear-gradient(90deg, #000 55%, transparent 100%);
            mask-image: linear-gradient(90deg, #000 55%, transparent 100%);
    opacity: .85;
  }
  .blur-photo {
    position: absolute; left: 0; bottom: 0; width: 540px; height: 340px;
    background: linear-gradient(180deg, rgba(255,255,255,0) 0%, #d5e0ea 45%, var(--sky) 100%);
  }

  .content { position: relative; padding: 52px 44px 0 60px; }
  .page--right .content { padding: 48px 44px 0 52px; }

  .headline { font: 700 26px/1.1 "Montserrat", sans-serif; color: var(--ink); }
  .strap { display: flex; align-items: flex-end; gap: 6px; margin: 4px 0 18px 150px; }
  .strap__num { font: 600 58px/0.9 "Oswald", sans-serif; color: var(--blue); }
  .strap__text { font: 600 19px/0.95 "Oswald", sans-serif; color: var(--blue-mid); text-transform: uppercase; padding-bottom: 4px; }

  .step { margin-bottom: 14px; }
  .step__head { display: flex; align-items: center; gap: 7px; margin-bottom: 4px; }
  .step__num {
    width: 19px; height: 19px; background: var(--blue); color: var(--paper);
    font: 600 12px/19px "Oswald", sans-serif; text-align: center;
  }
  .step__title { font: 600 16px/1 "Oswald", sans-serif; text-transform: uppercase; color: var(--ink); letter-spacing: .2px; }
  .step__body { margin-left: 26px; font: 400 12.5px/1.35 "Tinos", serif; color: var(--ink-soft); }
  .step__body p + p { margin-top: 6px; }
  .step__body ul { list-style: none; margin-top: 3px; }
  .step__body li::before { content: "•"; margin-right: 6px; }

  .offices { margin-top: 6px; font: 700 12.5px/1.3 "Tinos", serif; color: var(--ink); text-transform: uppercase; }
  .offices span { text-transform: none; font-weight: 400; }

  .intro { font: 400 12.5px/1.35 "Tinos", serif; color: var(--ink-soft); margin-bottom: 14px; }

  .folio { position: absolute; bottom: 18px; display: flex; align-items: center; gap: 6px; }
  .folio--left { left: 22px; }
  .folio--right { right: 22px; }
  .folio__num { background: var(--ink-soft); color: var(--paper); font: 600 10px/14px "Oswald", sans-serif; padding: 0 4px; }
  .folio__title { font: 700 11px/1 "Tinos", serif; color: var(--ink); }
</style>
</head>
<body>
<div class="spread">
  <section class="page page--left">
    <div class="hero-photo" role="img" aria-label="Businessman in a white shirt overlaid with a city skyline"></div>
    <div class="content">
      <h1 class="headline">So what’s the process?</h1>
      <div class="strap"><span class="strap__num">10</span><span class="strap__text">Steps<br>to success</span></div>

      <article class="step">
        <div class="step__head"><span class="step__num">1</span><h2 class="step__title">The initial phone call</h2></div>
        <div class="step__body">
          <p>The first step is the easiest one. Give us a call to find out if Headhunting, as a service, could be right for you.</p>
          <div class="offices">
            London: <span>+44 (0)20 7946 0312</span><br>
            Manchester: <span>+44 (0)161 496 0427</span><br>
            Birmingham: <span>+44 (0)121 496 0185</span><br>
            Southampton: <span>+44 (0)23 8049 6073</span><br>
            Edinburgh: <span>+44 (0)131 496 0258</span>
          </div>
        </div>
      </article>

      <article class="step">
        <div class="step__head"><span class="step__num">2</span><h2 class="step__title">The meeting</h2></div>
        <div class="step__body"><p>At our first meeting we’ll discuss the steps below and agree our strategy.</p></div>
      </article>

      <article class="step">
        <div class="step__head"><span class="step__num">3</span><h2 class="step__title">The brief</h2></div>
        <div class="step__body">
          <p>Following that meeting we’ll create an Assignment Report for your role. This document is an excellent touch-point for us both to make sure our mutual aims are consistent and enduring. The report will include:</p>
          <ul>
            <li>Our understanding of your business</li>
            <li>Key selling points of your organisation</li>
            <li>A detailed description of the position</li>
            <li>Criteria that you identify as ‘must haves’</li>
            <li>Types of company you’d like us to target</li>
            <li>The levels of confidentiality agreed</li>
            <li>Specific timescales for the assignment</li>
          </ul>
        </div>
      </article>

      <article class="step">
        <div class="step__head"><span class="step__num">4</span><h2 class="step__title">The research</h2></div>
        <div class="step__body"><p>We research those companies or organisations most likely to be employing your ideal candidate. By considering competitors and other relevant organisations or companies, we can narrow the field and highlight any potential areas of conflict (you may not want us Headhunting from within your group or customers for example).</p></div>
      </article>
    </div>
    <div class="folio folio--left"><span class="folio__num">26</span><span class="folio__title">Wexmoor Digest</span></div>
  </section>

  <section class="page page--right">
    <div class="blur-photo" role="img" aria-label="Soft blurred office scene in pale blue tones"></div>
    <div class="content">
      <p class="intro">Discreetly approaching candidates from competitors is one of our key capabilities and distinguishes us from recruitment agencies and other traditional hiring techniques.</p>

      <article class="step">
        <div class="step__head"><span class="step__num">5</span><h2 class="step__title">The identification</h2></div>
        <div class="step__body"><p>The goal is to identify the best, most successful individuals working within the appropriate field. We’ll ask you to approve our final list to make sure we’re not considering previous employees, and to identify anyone you’d rather we didn’t approach, or people that you’d like us to ‘fast track’.</p></div>
      </article>

      <article class="step">
        <div class="step__head"><span class="step__num">6</span><h2 class="step__title">The approach</h2></div>
        <div class="step__body"><p>Promoting your company and the benefits of the position, we’ll approach the candidates discreetly. Outcomes will be documented; we’ll feed these back to you – and take time to explain why candidates are, or are not, interested and suitable.</p></div>
      </article>

      <article class="step">
        <div class="step__head"><span class="step__num">7</span><h2 class="step__title">The approach</h2></div>
        <div class="step__body"><p>The goal is to identify the best, most successful individuals working within the appropriate field. We’ll ask you to approve our final list to make sure we’re not considering previous employees, and to identify anyone you’d rather we didn’t approach, or people that you’d like us to ‘fast track’.</p></div>
      </article>

      <article class="step">
        <div class="step__head"><span class="step__num">8</span><h2 class="step__title">The interviews with you</h2></div>
        <div class="step__body">
          <p>Our shortlist presents candidates for you to meet and interview. For each one, we’ll provide our summary report, a formatted CV (making it easier to facilitate comparisons), our interview notes, full details of their current salary / package and a copy of their psychometric profile.</p>
          <p>Your interviews can then focus on more nuanced requirements because every candidate you meet both can and would do your job. The Lead Consultant for your assignment will be happy to interview alongside you at this stage should you wish, at no additional cost.</p>
        </div>
      </article>

      <article class="step">
        <div class="step__head"><span class="step__num">9</span><h2 class="step__title">The liaison</h2></div>
        <div class="step__body"><p>The efficiency of this stage is often crucial to success. We’ll be working closely with you and your candidates during the interviews. When you make a decision we’ll offer consultation and act as a negotiator where required. We ensure everything runs smoothly so all parties feel comfortable.</p></div>
      </article>

      <article class="step">
        <div class="step__head"><span class="step__num">10</span><h2 class="step__title">The housekeeping</h2></div>
        <div class="step__body"><p>It’s a priority for us to handle rejections professionally and sensitively. Every candidate must be left with a positive impression of your organisation. Looking to the future, those candidates may be potential hires for a role yet to be defined in your business or a potential customer.</p></div>
      </article>
    </div>
    <div class="folio folio--right"><span class="folio__title">Wexmoor Digest</span><span class="folio__num">27</span></div>
  </section>
</div>
</body>
</html>
```